Wine Label for a Prosecco Wine Called Vuro

Prosecco is a white sparkling wine from Italy. We are looking for an eye catching, elegant label for this prosecco that is called "Vuro" because it is a young, fresh, lively white sparkling wine. (We do not want to see children or babies featured on the label-- just the name VURO please.) Attached is the old label for your reference, and the bottle type that will be used , which is a dark green Burgundy style bottle (pls ignore the label on the bottle). Please no grapes or wine glasses on the label. We are looking for something: eye catching / fun / ELEGANT (not cheap). We would be happy with a fun color too. Remember-- elegant, eye catching! Thanks!
Updates

Hi All, I think I made a mistake in my brief and have updated it. I also uploaded a competitor's label that we like very much to give better direction to what we are looking for. Also, the word Vuro cannot be vertical, nor can it be broken. It needs to read: VURO or Vuro. Thanks

Target Market(s)

American adults male and female.

Colors
abd036
33a6d7
33b8a4
ffcf3e

Requirements
Must have
• The mandatory information as shown on old labels. The word VURO should be very prominent.
Nice to have
• The uploaded photo of a competitor's prosecco shows a label we really like... if you could play around with this shape and style we'd be very happy.
Should not have
• No grape images, no wine glass images, no images of babies or children.

```html
<!DOCTYPE html>
<html lang="en">
<head>
<meta charset="utf-8">
<title>Vuro Prosecco DOC – Label Options</title>
<link href="https://fonts.googleapis.com/css2?family=Montserrat:wght@400;700&display=swap" rel="stylesheet">
<style>
  :root {
    --page-bg: #ffffff;
    --band-yellow: #f2c83c;
    --band-navy: #0e1226;
    --type-white: #ffffff;
    --type-gold: #c9a073;
    --fluid-blue: #4fb5e3;
    --fluid-yellow: #f6d460;
    --fluid-lilac: #b8a6e0;
    --mosaic-teal: #2fa3a8;
    --mosaic-orange: #f08a1c;
    --mosaic-red: #c8323c;
    --mosaic-violet: #5a3a9a;
  }
  * { margin: 0; padding: 0; box-sizing: border-box; }
  html, body {
    width: 1200px;
    height: 848px;
    overflow: hidden;
    background: var(--page-bg);
  }
  .label-sheet {
    position: relative;
    width: 1200px;
    height: 848px;
    display: flex;
    justify-content: center;
    align-items: center;
    gap: 60px;
  }
  .label {
    position: relative;
    width: 380px;
    height: 422px;
    overflow: hidden;
    font-family: "Montserrat", sans-serif;
  }

  /* Option one: fluid artwork with yellow band */
  .label--fluid .artwork {
    position: absolute;
    inset: 0;
    background:
      radial-gradient(ellipse at 20% 15%, var(--fluid-lilac) 0%, transparent 45%),
      radial-gradient(ellipse at 80% 85%, var(--fluid-yellow) 0%, transparent 50%),
      linear-gradient(160deg, var(--fluid-yellow) 0%, var(--fluid-blue) 35%, var(--fluid-lilac) 55%, var(--fluid-blue) 75%, var(--fluid-yellow) 100%);
  }
  .label--fluid .name-band {
    position: absolute;
    left: 0;
    right: 0;
    top: 148px;
    height: 124px;
    background: var(--band-yellow);
    display: flex;
    flex-direction: column;
    align-items: center;
    justify-content: center;
    color: var(--type-white);
  }

  /* Option two: mosaic artwork with navy band */
  .label--mosaic .artwork {
    position: absolute;
    left: 0;
    right: 0;
    top: 0;
    height: 298px;
    background:
      radial-gradient(ellipse at 45% 85%, var(--mosaic-orange) 0%, var(--mosaic-red) 22%, transparent 48%),
      radial-gradient(ellipse at 55% 30%, var(--mosaic-teal) 0%, transparent 55%),
      linear-gradient(135deg, var(--mosaic-orange) 0%, var(--mosaic-violet) 40%, var(--mosaic-teal) 70%, var(--mosaic-orange) 100%);
  }
  .label--mosaic .name-band {
    position: absolute;
    left: 0;
    right: 0;
    top: 298px;
    bottom: 0;
    background: var(--band-navy);
    display: flex;
    flex-direction: column;
    align-items: center;
    justify-content: center;
    color: var(--type-gold);
  }

  .wine-name {
    font-weight: 700;
    font-size: 54px;
    line-height: 1;
    letter-spacing: 0.42em;
    margin-right: -0.42em;
  }
  .wine-designation {
    font-weight: 400;
    font-size: 13px;
    letter-spacing: 0.55em;
    margin-right: -0.55em;
    margin-top: 10px;
  }
</style>
</head>
<body>
  <main class="label-sheet">
    <section class="label label--fluid">
      <div class="artwork" role="img" aria-label="Abstract fluid artwork of swirling yellow, blue and lilac oil-and-water colours with small bubbles"></div>
      <div class="name-band">
        <h1 class="wine-name">VURO</h1>
        <p class="wine-designation">PROSECCO DOC</p>
      </div>
    </section>

    <section class="label label--mosaic">
      <div class="artwork" role="img" aria-label="Abstract mosaic artwork of small iridescent tiles in teal, violet, orange and red"></div>
      <div class="name-band">
        <h2 class="wine-name">VURO</h2>
        <p class="wine-designation">PROSECCO DOC</p>
      </div>
    </section>
  </main>
</body>
</html>
```